Flyer for Custom Home Builder!

my company is Harlow Ridge Homes, I am looking for a flyer that we can send via email to a customer, or print and hand out. I am thinking four pages so we could print this and fold it., possibly creating a folder. The name of the company is Harlow Ridge Homes our website is here www.harlowridgehomes-example.com. Some text you can use "Crafting luxury homes isn't just a job, it's our passion.
With meticulous attention to detail and an unwavering commitment to using the finest materials, Harlow Ridge Homes consistently delivers exceptional results that stand as a testament to our commitment to quality."

"Trust is the cornerstone of our foundation.
With a proven track record of delivering on our promises for over 16 years, we prioritize transparent communication and integrity throughout every step of the home-building journey".

you may need to obtain the photos here
https://files.example-share.net/f/k27pw4m8zrt03xq61bnv/h?key=48vn2c9q1x7mb5t0ekd3h&dl=0

Target Market(s)

We build homes for every wealthy clients, therefore the photos are extremely important

Industry/Entity Type

Construction.

Requirements
Must have
• clear larger photos

```html
<!DOCTYPE html>
<html lang="en">
<head>
<meta charset="utf-8">
<title>Harlow Ridge Homes – Brochure Spreads</title>
<link href="https://fonts.googleapis.com/css2?family=Montserrat:wght@400;500;600&family=Playfair+Display:wght@400;700&display=swap" rel="stylesheet">
<style>
  :root {
    --stage: #6a6a6a;
    --paper: #ffffff;
    --ink: #1a1a1a;
    --text: #3a3a3a;
    --muted: #6e6e70;
    --brand: #4a4a4d;
    --black: #000000;
    --rule: #9a9a9a;
  }
  * { box-sizing: border-box; margin: 0; padding: 0; }
  html, body { width: 967px; height: 1200px; overflow: hidden; }
  body { background: var(--stage); position: relative; font-family: 'Montserrat', sans-serif; color: var(--text); }
  .abs { position: absolute; }
  .spread { position: absolute; left: 100px; width: 759px; height: 491px; background: var(--paper); overflow: hidden; }
  .spread-outer { top: 50px; }
  .spread-inner { top: 602px; }
  .center { text-align: center; }
  .serif { font-family: 'Playfair Display', serif; }
  .wordmark { font-family: 'Montserrat', sans-serif; font-weight: 600; color: var(--brand); text-transform: uppercase; letter-spacing: 2px; display: flex; align-items: center; gap: 6px; }
  .wordmark .mark { width: 9px; height: 9px; background: var(--brand); display: inline-block; }
  .url-box { border: 1px solid var(--ink); font-size: 9.5px; letter-spacing: 1px; color: var(--ink); display: flex; align-items: center; justify-content: center; background: var(--paper); }
  .rule { height: 1px; background: var(--rule); }

  /* outer spread */
  .cover-photo { left: 0; top: 0; width: 759px; height: 491px;
    background: linear-gradient(180deg, #8d939c 0%, #b8bcc1 30%, #d7d5cf 60%, #eeeeee 78%, #ffffff 92%); }
  .back-panel { left: 53px; top: 0; width: 281px; height: 491px; background: rgba(255,255,255,0.95); }
  .back-panel .fade { }
  .back-headline { font-weight: 700; font-size: 12.5px; line-height: 15.5px; color: var(--ink); text-transform: uppercase; }
  .back-intro { font-size: 8.4px; line-height: 13px; color: var(--text); }
  .back-name { font-size: 20px; font-weight: 700; color: var(--ink); }
  .back-detail { font-size: 9.5px; line-height: 15px; font-weight: 500; color: var(--text); text-transform: uppercase; }
  .cover-name { font-size: 30px; font-weight: 700; color: var(--black); white-space: nowrap; }

  /* inner spread */
  .black-panel { left: 0; top: 0; width: 201px; height: 491px; background: var(--black); color: #fff; }
  .pool-photo { left: 10px; top: 14px; width: 402px; height: 243px; background: linear-gradient(180deg, #b9c9d6 0%, #e6e2dc 35%, #a89a88 55%, #7fb8c6 78%, #5fa4b8 100%); }
  .passion-head { font-size: 15px; line-height: 18px; color: #fff; }
  .black-body { font-size: 7px; line-height: 9px; color: #e8e8e8; text-align: justify; }
  .why-title { font-size: 10px; color: var(--text); letter-spacing: 0.3px; }
  .service-icon { width: 27px; height: 27px; }
  .service-title { font-size: 10.5px; font-weight: 500; line-height: 12.5px; color: var(--ink); text-transform: uppercase; }
  .service-sub { font-size: 8px; line-height: 10px; color: var(--ink); }
  .mid-note { font-size: 7.3px; line-height: 9px; color: var(--muted); text-align: justify; }
  .trust-head { font-size: 15px; color: var(--ink); }
  .trust-lead { font-size: 8.3px; line-height: 10.5px; font-weight: 600; color: var(--ink); text-align: justify; }
  .trust-body { font-size: 7px; line-height: 10.6px; color: var(--text); text-align: justify; }
  .aerial-photo { left: 389px; top: 269px; width: 361px; height: 132px; background: linear-gradient(180deg, #2f3a44 0%, #4b5157 30%, #c7c1b6 60%, #6f6c68 100%); }
  .thumb { top: 410px; height: 72px; }
  .thumb-living { left: 389px; width: 116px; background: linear-gradient(180deg, #d9d9d6 0%, #f2f0ec 50%, #b9a58c 100%); }
  .thumb-dusk { left: 512px; width: 116px; background: linear-gradient(180deg, #7b7fa6 0%, #d59aa3 40%, #4d4f57 70%, #8e8f94 100%); }
  .thumb-bath { left: 634px; width: 111px; background: linear-gradient(180deg, #eeece9 0%, #e3dfd9 55%, #c79b62 100%); }
</style>
</head>
<body>

<!-- Outer spread: back page + cover -->
<section class="spread spread-outer">
  <div class="abs cover-photo" role="img" aria-label="Modern two-storey home with dark siding, white stone and large lit windows at dusk, fading to white at the bottom"></div>

  <div class="abs back-panel">
    <div class="abs wordmark" style="left:0;width:281px;top:52px;justify-content:center;font-size:13px;"><span class="mark"></span>Harlow Ridge Homes</div>
    <p class="abs serif back-headline center" style="left:10px;width:261px;top:93px;">You don’t just have one person<br>in your corner—you have many.</p>
    <p class="abs back-intro center" style="left:14px;width:253px;top:130px;">As true mavens of custom home design we focus on transcending initial “Dream Home” concepts to fashion award winning and impeccably curated luxurious living environments for our exclusive clientele.</p>
    <p class="abs serif back-name center" style="left:0;width:281px;top:196px;">Harlow Ridge Homes</p>
    <p class="abs back-detail center" style="left:0;width:281px;top:234px;">(555) 014-2276</p>
    <div class="abs rule" style="left:98px;width:84px;top:257px;"></div>
    <p class="abs back-detail center" style="left:0;width:281px;top:264px;">480 Cedar Bend Road, Suite 200,<br>Austin TX 78730</p>
    <div class="abs rule" style="left:98px;width:84px;top:303px;"></div>
    <p class="abs back-detail center" style="left:0;width:281px;top:308px;text-transform:none;">Open hours<br>MON - FRI, 9 AM - 5 PM</p>
    <p class="abs back-intro center" style="left:14px;width:253px;top:358px;">From a secluded technological utopia or magnificent country estate, to a rustic hillside ranch, lakefront retreat, or masterpiece chateau in an exclusive Austin area neighborhood, Harlow Ridge Homes creates distinctive architectural wonders. Call us today!</p>
    <div class="abs url-box" style="left:49px;width:182px;top:451px;height:18px;font-size:8px;letter-spacing:0.6px;">www.harlowridgehomes-example.com</div>
  </div>

  <div class="abs wordmark" style="left:379px;width:380px;top:369px;justify-content:center;font-size:15px;"><span class="mark"></span>Harlow Ridge Homes</div>
  <p class="abs serif cover-name center" style="left:379px;width:380px;top:404px;">Harlow Ridge Homes</p>
  <div class="abs url-box" style="left:476px;width:186px;top:451px;height:18px;font-size:8px;letter-spacing:0.6px;">www.harlowridgehomes-example.com</div>
</section>

<!-- Inner spread -->
<section class="spread spread-inner">
  <div class="abs black-panel"></div>
  <div class="abs pool-photo" role="img" aria-label="Modern home terrace with infinity pool, spa, outdoor lounge and fireplace"></div>

  <p class="abs serif passion-head" style="left:13px;width:185px;top:272px;">Crafting luxury homes isn't just a job, it's our passion.</p>
  <div class="abs" style="left:13px;width:30px;top:318px;height:1px;background:#fff;"></div>
  <p class="abs black-body" style="left:12px;width:178px;top:325px;">With meticulous attention to detail and an unwavering commitment to using the finest materials, Harlow Ridge Homes consistently delivers exceptional results that stand as a testament to our commitment to quality.</p>
  <p class="abs black-body" style="left:12px;width:178px;top:380px;">At Harlow Ridge Homes, we specialize in creating exceptional, one-of-a-kind homes that are tailored to your unique vision and lifestyle. Whether you dream of a secluded technological utopia, a magnificent country estate, a rustic hillside ranch, a lakefront retreat, or a masterpiece chateau in an exclusive Austin area neighborhood, we can bring your vision to life.</p>
  <div class="abs" style="left:13px;width:178px;top:466px;height:1px;background:#bbb;"></div>
  <p class="abs" style="left:0;width:201px;top:472px;font-size:8.3px;color:#fff;text-align:center;">www.harlowridgehomes-example.com</p>

  <p class="abs serif why-title" style="left:210px;top:280px;">WHY HARLOW RIDGE HOMES?</p>

  <svg class="abs service-icon" style="left:206px;top:293px;" viewBox="0 0 27 27" aria-hidden="true">
    <circle cx="13.5" cy="13.5" r="12.5" fill="#8a8a8a"/><circle cx="13.5" cy="13.5" r="9.5" fill="none" stroke="#fff" stroke-width="0.8"/>
    <path d="M8.5 13 L13.5 8.5 L18.5 13 M10 12 V18 H17 V12 M12.3 18 V14.5 H14.7 V18" fill="none" stroke="#fff" stroke-width="0.9"/>
  </svg>
  <p class="abs service-title" style="left:240px;top:299px;">Harlow Ridge<br>Design/Build</p>
  <p class="abs service-sub" style="left:240px;top:327px;">Your lot or our<br>Design · Built · Enjoy</p>

  <svg class="abs service-icon" style="left:206px;top:350px;" viewBox="0 0 27 27" aria-hidden="true">
    <circle cx="13.5" cy="13.5" r="12.5" fill="#8a8a8a"/><circle cx="13.5" cy="13.5" r="9.5" fill="none" stroke="#fff" stroke-width="0.8"/>
    <rect x="9" y="9" width="9" height="9" fill="none" stroke="#fff" stroke-width="0.9"/>
    <path d="M11 15.5 L15.5 11 M14 11 H15.5 V12.5" fill="none" stroke="#fff" stroke-width="0.9"/>
  </svg>
  <p class="abs service-title" style="left:240px;top:356px;">Harlow Ridge<br>High End Remodels</p>
  <p class="abs service-sub" style="left:240px;top:384px;">Interior &amp; Exterior<br>Partial or Complete<br>Home Remodeling</p>

  <p class="abs mid-note" style="left:210px;width:159px;top:418px;">As true mavens of custom home design we focus on transcending initial “Dream Home” concepts to fashion award winning and impeccably curated luxurious living environments for our exclusive clientele.</p>
  <div class="abs rule" style="left:210px;width:159px;top:465px;background:#ccc;"></div>
  <p class="abs" style="left:210px;width:159px;top:473px;font-size:9px;color:var(--ink);display:flex;align-items:center;justify-content:center;gap:5px;">
    <svg width="9" height="9" viewBox="0 0 24 24" aria-hidden="true"><circle cx="12" cy="12" r="11" fill="none" stroke="#1a1a1a" stroke-width="2"/><path d="M8.5 6.5 L10.5 6.5 L11.5 9 L10 10.2 C10.8 11.9 12.1 13.2 13.8 14 L15 12.5 L17.5 13.5 V15.5 C17.5 16.5 16.5 17.3 15.5 17.1 C11 16.3 7.7 13 6.9 8.5 C6.7 7.5 7.5 6.5 8.5 6.5 Z" fill="#1a1a1a"/></svg>
    (555) 014-2276
  </p>

  <div class="abs rule" style="left:412px;width:187px;top:26px;background:#777;"></div>
  <div class="abs wordmark" style="left:606px;width:148px;top:20px;justify-content:flex-end;font-size:10px;letter-spacing:1.2px;"><span class="mark" style="width:7px;height:7px;"></span>Harlow Ridge Homes</div>
  <p class="abs serif trust-head" style="left:430px;top:57px;">Trust is the cornerstone of our foundation.</p>
  <div class="abs rule" style="left:430px;width:28px;top:78px;background:#555;"></div>
  <p class="abs trust-lead" style="left:428px;width:316px;top:84px;">With a proven track record of delivering on our promises for over 16 years, we prioritize transparent communication and integrity throughout every step of the home-building journey</p>
  <p class="abs trust-body" style="left:428px;width:316px;top:127px;">Harlow Ridge Homes is a premier custom home builder committed to creating exceptional, one-of-a-kind homes that reflect the unique vision and style of our clients. With over two decades of experience in the industry, we have earned a reputation for unparalleled craftsmanship and attention to detail, resulting in homes that are both luxurious and functional.</p>
  <p class="abs trust-body" style="left:428px;width:316px;top:191px;">We work closely with our clients from start to finish to ensure that every detail is carefully considered and executed to perfection, resulting in homes that exceed our clients' expectations. At Harlow Ridge Homes, we believe in creating homes that are as individual as our clients, and we are dedicated to providing exceptional service and quality craftsmanship to every project we take on.</p>

  <div class="abs aerial-photo" role="img" aria-label="Aerial view of a large white stone estate home with tiled roofs at dusk"></div>
  <div class="abs thumb thumb-living" role="img" aria-label="Bright open-plan living and dining room"></div>
  <div class="abs thumb thumb-dusk" role="img" aria-label="Outdoor lounge and pool of a modern home under a pink sunset sky"></div>
  <div class="abs thumb thumb-bath" role="img" aria-label="Bathroom with wooden vanity, mirrors and open shelving"></div>
</section>

</body>
</html>
```